Finance Broker helping people meet their personal and business goals

New business card design,
1st look at the old business card so this makes sense.
I DON'T want:
the subtext "For all your Rural and Commercial Finance".
I DON'T want the: "and Management Consultant" words
I DON'T want the old phone: 07 48213957
I DON'T want the fax number: 07 45826031
I DON'T want the email address: tallowcreek@brightlink.com.au
I DON'T want the flower
What I DO want
I DO want the mobile 0451 836 209 (in larger text)
I DO want:
My name: Dennis Harwell-Lowe
I DO want: Australian Credit Licence 529164 (Tallow Creek Pty Ltd)
I DO want: Principal Finance Broker
I DO want new email: dennis@plotnextstep.com.au
I DO want address: PO Box 928, Tully Qld 4854
I DO want the existing logo (PNS on existing card)

Target Market(s)

Business Borrowers, Home Purchasers, and People wanting to finance cars and plant and equipment

Industry/Entity Type

Financial Service

Contact Information for Business Card

See project description

Font styles to use
Serif

Colors

Designer to choose colors to be used in the design.

Requirements
Must have
• See project description
Nice to have
• Black and Yellow colours
Should not have
• See project description

```html
<!DOCTYPE html>
<html lang="en">
<head>
<meta charset="utf-8">
<title>Plot Next Step – Business Card</title>
<link rel="stylesheet" href="https://fonts.googleapis.com/css2?family=Tinos:wght@400;700&family=Questrial&display=swap">
<style>
  :root {
    --backdrop: #a7a7a7;
    --card: #262b29;
    --card-edge: #303634;
    --accent: #dfe35a;
    --ink-light: #f2f2f2;
    --ink-dark: #1d211f;
    --paper: #ffffff;
  }
  * { margin: 0; padding: 0; box-sizing: border-box; }
  html, body {
    width: 1200px; height: 930px; overflow: hidden;
    background: var(--backdrop);
  }
  .stage { position: relative; width: 1200px; height: 930px; }
  .card {
    position: absolute; width: 700px; height: 400px;
    background: linear-gradient(160deg, var(--card-edge), var(--card) 60%);
    border-radius: 24px; overflow: hidden;
    box-shadow: 0 8px 20px rgba(0,0,0,.35);
  }
  .card--front { left: 60px; top: 50px; }
  .card--back { left: 440px; top: 480px; }

  .brand { position: absolute; display: flex; align-items: center; gap: 14px; }
  .brand__text { display: flex; flex-direction: column; }
  .brand__name {
    font-family: "Tinos", serif; font-weight: 400;
    color: var(--accent); font-size: 40px; line-height: 1;
  }
  .brand__tagline {
    font-family: "Questrial", sans-serif; color: var(--ink-light);
    font-size: 15px; letter-spacing: .5px; margin-top: 6px; margin-left: 10px;
  }
  .brand__dot { width: 44px; height: 44px; border-radius: 50%; background: var(--accent); }

  .card--front .brand { left: 170px; top: 160px; }
  .card--back .brand { left: 40px; top: 108px; }
  .card--back .brand__name { font-size: 32px; }
  .card--back .brand__tagline { font-size: 12px; }
  .card--back .brand__dot { width: 36px; height: 36px; }

  .person { position: absolute; right: 26px; top: 60px; text-align: right; font-family: "Tinos", serif; }
  .person__name { color: var(--accent); font-size: 30px; text-transform: uppercase; letter-spacing: .5px; }
  .person__role, .person__licence { color: var(--ink-light); font-size: 20px; line-height: 1.3; }

  .divider { position: absolute; left: 0; right: 26px; top: 200px; height: 1.5px; background: var(--accent); }

  .contact {
    position: absolute; left: 40px; top: 262px;
    font-family: "Tinos", serif; color: var(--ink-light); font-size: 22px; line-height: 1.3;
  }
  .footer-strip { position: absolute; left: 0; bottom: 0; width: 460px; height: 30px; background: var(--paper); }
  .phone-box {
    position: absolute; right: 0; bottom: 0; width: 240px; height: 110px;
    background: var(--accent); display: flex; align-items: center; justify-content: center;
    font-family: "Tinos", serif; font-weight: 700; font-size: 30px; color: var(--ink-dark);
  }
</style>
</head>
<body>
<div class="stage">
  <section class="card card--front">
    <div class="brand">
      <div class="brand__text">
        <span class="brand__name">Plot Next Step</span>
        <span class="brand__tagline">A Member of the Tallow Creek Group</span>
      </div>
      <span class="brand__dot"></span>
    </div>
  </section>

  <section class="card card--back">
    <div class="brand">
      <div class="brand__text">
        <span class="brand__name">Plot Next Step</span>
        <span class="brand__tagline">A Member of the Tallow Creek Group</span>
      </div>
      <span class="brand__dot"></span>
    </div>
    <div class="person">
      <div class="person__name">Dennis Harwell-Lowe</div>
      <div class="person__role">Principal Finance Broker</div>
      <div class="person__licence">Australian Credit Licence 529164</div>
    </div>
    <div class="divider"></div>
    <div class="contact">
      <div>dennis@plotnextstep.com.au</div>
      <div>PO Box 928, Tully Qld 4854</div>
    </div>
    <div class="footer-strip"></div>
    <div class="phone-box">0451 836 209</div>
  </section>
</div>
</body>
</html>
```